Australian residential property business needs a business card design

I need a business card design for my new business 'Harbour Estate Ventures'. The business will involve house purchases, land development sites, renovation projects, sub-divisions etc. I will be buying property from motivated vendors and working with property investors. I will deal with a wide range of people working in the residential property market including real estate agents, councils, tradespeople, banks, home owners, etc.

I would like something simple, not flashy, but a little bit unique. The colours should be in line with my logo. The business card needs to be professional. I would like something memorable, but not 'busy' or too bright. Not boring. Modern ok.

Target Market(s)

Home owners looking to sell their property, real estate agents, tradespeople (e.g. plumbers, builders, electricians etc), property investors, local councils, and anyone else involved in the residential property industry

Industry/Entity Type

Business

Contact Information for Business Card

I need to include my business name/logo, my name, my title, a PO Box number/address, a mobile number, and an email address.

Font styles to use
Serif

Requirements
Must have
• My business card details listed above.

```html
<!DOCTYPE html>
<html lang="en">
<head>
<meta charset="utf-8">
<title>Harbour Estate Ventures – Business Cards</title>
<link rel="stylesheet" href="https://fonts.googleapis.com/css2?family=Open+Sans:wght@400;700&display=swap">
<style>
  :root {
    --bg: #d9d8d5;
    --card-white: #ffffff;
    --gold: #f0b323;
    --green: #1f7a34;
    --orange: #ee7a12;
    --ink: #3a3a3a;
    --white: #ffffff;
  }
  * { margin: 0; padding: 0; box-sizing: border-box; }
  html, body {
    width: 1200px; height: 1001px; overflow: hidden;
    background: var(--bg);
    font-family: "Open Sans", Arial, sans-serif;
  }
  .canvas { position: relative; width: 1200px; height: 1001px; }

  .card {
    position: absolute;
    width: 494px; height: 304px;
    background: var(--card-white);
    overflow: hidden;
  }
  .card--front { left: 351px; top: 119px; }
  .card--back  { left: 353px; top: 475px; }

  /* brand block: square above the name */
  .brand {
    position: absolute;
    display: flex; flex-direction: column; align-items: center; justify-content: center; gap: 10px;
    font-weight: 700; color: var(--orange);
    text-transform: uppercase; text-align: center;
    font-size: 21px; line-height: 1.15;
  }
  .brand__mark { width: 30px; height: 30px; background: var(--green); flex: none; }

  /* front card */
  .front__panel {
    position: absolute; left: 243px; top: 0; right: 0; bottom: 0;
    background: var(--gold);
  }
  .card--front .brand { left: 0; width: 243px; top: 80px; height: 130px; }
  .front__web {
    position: absolute; left: 0; width: 243px; top: 276px;
    text-align: center; color: var(--green); font-size: 16px;
  }

  .contact {
    position: absolute; list-style: none;
    font-size: 13px; line-height: 1;
  }
  .contact li { display: flex; align-items: center; gap: 6px; height: 19px; }
  .contact .icon { width: 13px; height: 13px; flex: none; }
  .card--front .contact { left: 289px; top: 128px; color: var(--white); }
  .card--front .icon__box { fill: var(--white); }
  .card--front .icon__glyph { fill: var(--gold); }

  /* back card */
  .back__frame {
    position: absolute; left: 27px; top: 58px; width: 234px; height: 142px;
    border: 3px solid var(--green);
  }
  .card--back .brand { left: 30px; width: 228px; top: 61px; height: 136px; }
  .card--back .contact { left: 296px; top: 94px; color: var(--ink); }
  .card--back .icon__box { fill: var(--gold); }
  .card--back .icon__glyph { fill: var(--white); }

  .back__rule {
    position: absolute; left: 0; right: 0; top: 252px; height: 2px; background: var(--gold);
  }
  .back__band {
    position: absolute; left: 0; right: 0; top: 258px; height: 26px;
    background: var(--gold);
    color: var(--white); font-size: 15px; letter-spacing: 12px;
    text-align: center; line-height: 26px; padding-left: 12px;
  }
</style>
</head>
<body>
<main class="canvas">
  <section class="card card--front">
    <div class="brand"><span class="brand__mark"></span><span>Harbour Estate<br>Ventures</span></div>
    <p class="front__web">www.website.com</p>
    <div class="front__panel"></div>
    <ul class="contact">
      <li><svg class="icon" viewBox="0 0 16 16"><rect class="icon__box" width="16" height="16"/><circle class="icon__glyph" cx="8" cy="5.5" r="2.8"/><path class="icon__glyph" d="M3 14c0-3 2.2-5 5-5s5 2 5 5z"/></svg>name, title</li>
      <li><svg class="icon" viewBox="0 0 16 16"><rect class="icon__box" width="16" height="16"/><path class="icon__glyph" d="M8 2a4 4 0 0 0-4 4c0 3 4 8 4 8s4-5 4-8a4 4 0 0 0-4-4zm0 5.5A1.5 1.5 0 1 1 8 4.5a1.5 1.5 0 0 1 0 3z"/></svg>PO Box number/address</li>
      <li><svg class="icon" viewBox="0 0 16 16"><rect class="icon__box" width="16" height="16"/><path class="icon__glyph" d="M5 3h3l-1 3-1.2.6c.6 1.6 1.6 2.6 3.2 3.2L9.6 8.6l3 1v3c-5 .4-8-2.6-7.6-9.6z"/></svg>mobile number</li>
      <li><svg class="icon" viewBox="0 0 16 16"><rect class="icon__box" width="16" height="16"/><rect class="icon__glyph" x="3" y="4.5" width="10" height="7"/><path class="icon__box" d="M3 4.5l5 4 5-4v1l-5 4-5-4z"/></svg>email address</li>
    </ul>
  </section>

  <section class="card card--back">
    <div class="back__frame"></div>
    <div class="brand"><span class="brand__mark"></span><span>Harbour Estate<br>Ventures</span></div>
    <ul class="contact">
      <li><svg class="icon" viewBox="0 0 16 16"><rect class="icon__box" width="16" height="16"/><circle class="icon__glyph" cx="8" cy="5.5" r="2.8"/><path class="icon__glyph" d="M3 14c0-3 2.2-5 5-5s5 2 5 5z"/></svg>Name, title</li>
      <li><svg class="icon" viewBox="0 0 16 16"><rect class="icon__box" width="16" height="16"/><path class="icon__glyph" d="M8 2a4 4 0 0 0-4 4c0 3 4 8 4 8s4-5 4-8a4 4 0 0 0-4-4zm0 5.5A1.5 1.5 0 1 1 8 4.5a1.5 1.5 0 0 1 0 3z"/></svg>PO Box number/address</li>
      <li><svg class="icon" viewBox="0 0 16 16"><rect class="icon__box" width="16" height="16"/><path class="icon__glyph" d="M5 3h3l-1 3-1.2.6c.6 1.6 1.6 2.6 3.2 3.2L9.6 8.6l3 1v3c-5 .4-8-2.6-7.6-9.6z"/></svg>mobile number</li>
      <li><svg class="icon" viewBox="0 0 16 16"><rect class="icon__box" width="16" height="16"/><rect class="icon__glyph" x="3" y="4.5" width="10" height="7"/><path class="icon__box" d="M3 4.5l5 4 5-4v1l-5 4-5-4z"/></svg>email address</li>
    </ul>
    <div class="back__rule"></div>
    <p class="back__band">www.website.com</p>
  </section>
</main>
</body>
</html>
```